Cedar Hall businesscard

We changed our name and logo, now we need new business cards.
3-4/72 Marlow Street Fernvale 2763
www.cedarhall-example.org.au
info@cedarhall-example.org.au
Lorna-Jean Whitcombe
Senior Pastor
ph: 02 95874210

```html
<!DOCTYPE html>
<html lang="en">
<head>
<meta charset="utf-8">
<title>Cedar Hall – Business Card</title>
<link rel="stylesheet" href="https://fonts.googleapis.com/css2?family=Lato:wght@400;700&display=swap">
<style>
  :root {
    --page-bg: #ffffff;
    --card-bg: #ffffff;
    --brand-blue: #5f8799;
    --ink-light: #ffffff;
    --navy-deep: #1c3658;
    --blue-mid: #4a6f93;
    --blue-soft: #6f92b2;
    --teal: #3f7a7c;
  }
  html, body {
    margin: 0;
    padding: 0;
    width: 1200px;
    height: 1000px;
    overflow: hidden;
    background: var(--page-bg);
  }
  .canvas {
    position: relative;
    width: 1200px;
    height: 1000px;
  }
  .business-card {
    position: absolute;
    left: 342px;
    top: 77px;
    width: 518px;
    height: 845px;
    background: var(--card-bg);
    box-shadow: 0 1px 4px rgba(0,0,0,0.25);
    overflow: hidden;
    font-family: "Lato", Arial, sans-serif;
    color: var(--ink-light);
  }
  .card-artwork {
    position: absolute;
    inset: 0;
    display: block;
  }
  .brand {
    position: absolute;
    left: 0;
    top: 190px;
    width: 518px;
    display: flex;
    align-items: center;
    justify-content: center;
    gap: 16px;
  }
  .brand-dot {
    width: 30px;
    height: 30px;
    border-radius: 50%;
    background: var(--brand-blue);
  }
  .brand-name {
    font-weight: 700;
    font-size: 44px;
    line-height: 52px;
    letter-spacing: 1px;
    text-transform: uppercase;
    color: var(--brand-blue);
  }
  .contact-block {
    position: absolute;
    left: 0;
    top: 489px;
    width: 518px;
    text-align: center;
    font-size: 24px;
    line-height: 33px;
  }
  .contact-block p { margin: 0; }
  .person-name {
    font-weight: 700;
    font-size: 28px;
    line-height: 36px;
    text-transform: uppercase;
  }
  .person-role {
    font-weight: 700;
    font-size: 24px;
    line-height: 34px;
    text-transform: uppercase;
    margin-bottom: 16px !important;
  }
  .phone { margin-bottom: 19px !important; }
  .address { margin-bottom: 19px !important; }
  .label { font-weight: 700; }
</style>
</head>
<body>
<div class="canvas">
  <div class="business-card">
    <svg class="card-artwork" width="518" height="845" viewBox="0 0 518 845">
      <defs>
        <linearGradient id="panelGradient" x1="0" y1="0" x2="1" y2="0.3">
          <stop offset="0" stop-color="var(--navy-deep)"/>
          <stop offset="0.4" stop-color="var(--blue-mid)"/>
          <stop offset="0.75" stop-color="var(--blue-soft)"/>
          <stop offset="1" stop-color="var(--teal)"/>
        </linearGradient>
      </defs>
      <path class="pattern-panel" role="img" aria-label="Decorative swirling floral damask pattern in navy, blue and teal"
            d="M0 358 Q259 538 518 358 L518 845 L0 845 Z" fill="url(#panelGradient)"/>
    </svg>

    <div class="brand">
      <span class="brand-dot"></span>
      <span class="brand-name">Cedar Hall</span>
    </div>

    <div class="contact-block">
      <p class="person-name">Lorna-Jean Whitcombe</p>
      <p class="person-role">Senior Pastor</p>
      <p class="phone"><span class="label">P</span> 02 95874210</p>
      <p class="address">3-4/72 Marlow Street<br>Fernvale NSW 2763</p>
      <p class="web"><span class="label">W</span> www.cedarhall-example.org.au</p>
      <p class="email"><span class="label">E</span> info@cedarhall-example.org.au</p>
    </div>
  </div>
</div>
</body>
</html>
```